coralridge studio business card

Architectural firm business card

Please note:

corporate colour black+yellow are the only elements to be kept.
NO OTHER ELEMENT TO BE REUSED FROM PREVIOUS BUSINESS CARD.
Thank you.

Dear Everyone,

Thank you for your participation. I have upload the KVLT+ logo again for incoporate in the card. in tif and pdf format.

Thank you 

I keep getting request for the logo file. Does everyone has the same problem?

I cannot do much, because the file is upload to the website server. I can't seem to see it either.

The logo file is now working. Please download. I check it myself. Thank you everyone.

Dear All,

Thank you for all the hard work. There are a lot of great work. Due to current commitment with work, I am unable to review them just yet. I will do so next week and advise everyone also. Thank you again. Best regards

Dear All,

Thank you for your participation. There are a lot of good design. Unfortunately, I can only select one. All the best. This is definitely a good crowd to work with. Thank you everyone again.

Best regards

Target Market(s)

Corporate, commercial and institutional projects only

Industry/Entity Type

Business

Requirements
Must have
• elegant simple
double sided with coating
Member of Southern Guild of Draftsmen (logo only)
corporate colour black and

LOGO FILE UPLOADED
Should not have
• should not be the same as current business card.
upload for reference information only.
font sans serif preferred.

```html
<!DOCTYPE html>
<html lang="en">
<head>
<meta charset="utf-8">
<title>Coralridge Studio — Business Card</title>
<link rel="stylesheet" href="https://fonts.googleapis.com/css2?family=Source+Sans+3:wght@400;600;700&display=swap">
<style>
  :root {
    --orange: #f08a24;
    --orange-deep: #e9771a;
    --orange-glow: #ffe3a6;
    --ink: #1d1d1d;
    --charcoal: #2a2a2a;
    --paper: #ffffff;
    --stage-light: #f4f4f4;
    --stage-dark: #bdbdbd;
    --muted: #555555;
  }
  * { box-sizing: border-box; margin: 0; padding: 0; }
  html, body { width: 1200px; height: 646px; overflow: hidden; }
  body {
    font-family: "Source Sans 3", "Myriad Pro", sans-serif;
    background: linear-gradient(160deg, var(--stage-light) 0%, #e2e2e2 55%, var(--stage-dark) 100%);
    position: relative;
  }
  .card {
    position: absolute;
    top: 164px;
    width: 520px;
    height: 318px;
    overflow: hidden;
    box-shadow: 0 12px 30px rgba(0,0,0,.22);
  }
  /* ---------- Front ---------- */
  .card--front {
    left: 50px;
    background: radial-gradient(ellipse 60% 70% at 48% 34%, var(--orange-glow) 0%, #fbb35a 40%, var(--orange) 75%, var(--orange-deep) 100%);
  }
  .front__stripes { position: absolute; inset: 0; }
  .front__brand {
    position: absolute;
    left: 0; right: 0; top: 112px;
    text-align: center;
  }
  .brand-name {
    display: inline-flex;
    align-items: center;
    gap: 8px;
    font-weight: 700;
    font-size: 26px;
    letter-spacing: .5px;
    color: var(--ink);
  }
  .brand-name__square {
    width: 16px; height: 16px;
    background: var(--orange-deep);
  }
  .front__tagline {
    margin-top: 8px;
    font-size: 14px;
    color: var(--charcoal);
    letter-spacing: .3px;
  }
  .front__web {
    position: absolute;
    left: 0; right: 0; bottom: 26px;
    text-align: center;
    font-size: 17px;
    font-weight: 600;
    color: var(--paper);
    letter-spacing: .4px;
  }
  /* ---------- Back ---------- */
  .card--back { left: 630px; background: var(--paper); }
  .back__decor { position: absolute; inset: 0; }
  .back__brand {
    position: absolute;
    left: 30px; top: 150px;
  }
  .back__brand .brand-name { font-size: 22px; }
  .back__services {
    margin-top: 6px;
    padding-left: 24px;
    list-style: none;
    font-size: 14px;
    line-height: 1.15;
    color: var(--orange);
  }
  .person {
    position: absolute;
    left: 262px; top: 28px;
  }
  .person__name {
    font-size: 24px;
    font-weight: 700;
    color: var(--ink);
  }
  .person__post { font-size: 11px; font-weight: 400; color: var(--muted); margin-left: 4px; }
  .person__reg { font-size: 11px; color: var(--muted); }
  .person__role { font-size: 15px; color: var(--orange); line-height: 1.2; }
  .person__mobile { font-size: 15px; font-weight: 600; color: var(--ink); }
  .contacts {
    position: absolute;
    left: 262px; top: 136px;
    display: grid;
    grid-template-columns: 20px 1fr;
    column-gap: 10px;
    row-gap: 4px;
    align-items: center;
    font-size: 12.5px;
    color: var(--ink);
  }
  .contacts svg { width: 16px; height: 16px; fill: var(--orange); }
  .contacts__address { line-height: 1.15; font-weight: 600; }
  .back__base {
    position: absolute;
    left: 0; right: 0; bottom: 0;
    height: 24px;
    background: var(--ink);
  }
</style>
</head>
<body>

<section class="card card--front" aria-label="Card front">
  <svg class="front__stripes" viewBox="0 0 520 318" aria-hidden="true">
    <polygon points="420,0 440,0 500,318 480,318" fill="rgba(255,255,255,.14)"/>
    <polygon points="450,0 458,0 518,318 510,318" fill="rgba(255,255,255,.12)"/>
  </svg>
  <div class="front__brand">
    <div class="brand-name"><span class="brand-name__square"></span>Coralridge Studio</div>
    <p class="front__tagline">architects | urban designers | project managers</p>
  </div>
  <p class="front__web">www.coralridgestudio.com.au</p>
</section>

<section class="card card--back" aria-label="Card back">
  <svg class="back__decor" viewBox="0 0 520 318" aria-hidden="true">
    <rect x="20" y="20" width="200" height="240" fill="#fdeee0"/>
    <polygon points="440,0 462,0 520,240 520,294 500,294" fill="rgba(240,138,36,.10)"/>
    <polygon points="420,230 520,210 520,294 400,294" fill="var(--orange)"/>
    <line x1="448" y1="210" x2="464" y2="294" stroke="#fff" stroke-width="1.5"/>
    <line x1="458" y1="208" x2="474" y2="294" stroke="#fff" stroke-width="1"/>
  </svg>

  <div class="back__brand">
    <div class="brand-name"><span class="brand-name__square"></span>Coralridge Studio</div>
    <ul class="back__services">
      <li>architects</li>
      <li>urban designers</li>
      <li>project managers</li>
    </ul>
  </div>

  <div class="person">
    <p class="person__name">Linh Harper<span class="person__post">kvlt, ipmx</span></p>
    <p class="person__reg">Architect (NSW BoA reg. no: 7312)</p>
    <p class="person__role">Director</p>
    <p class="person__mobile">M 0412 555 017</p>
  </div>

  <div class="contacts">
    <svg viewBox="0 0 16 16" aria-label="Phone"><path d="M3 1h3l1 4-2 1.5a9 9 0 0 0 4.5 4.5L11 9l4 1v3a2 2 0 0 1-2 2A12 12 0 0 1 1 3a2 2 0 0 1 2-2z"/></svg>
    <span>+612 9555 0142</span>
    <svg viewBox="0 0 16 16" aria-label="Fax"><path d="M4 1h8v4H4zM1 6h14v7h-3v2H4v-2H1zM5 10v3h6v-3z"/></svg>
    <span>+612 9555 0143</span>
    <svg viewBox="0 0 16 16" aria-label="Email"><path d="M1 3h14v10H1zM2 4l6 5 6-5v1L8 10 2 5z" fill-rule="evenodd"/></svg>
    <span>hello@coralridgestudio.com.au</span>
    <svg viewBox="0 0 16 16" aria-label="Website"><circle cx="8" cy="8" r="7"/><path d="M1 8h14M8 1c-3 4-3 10 0 14M8 1c3 4 3 10 0 14" stroke="#fff" stroke-width="1" fill="none"/></svg>
    <span>www.coralridgestudio.com.au</span>
    <svg viewBox="0 0 16 16" aria-label="Address"><path d="M8 1l7 7h-2v7H9v-4H7v4H3V8H1z"/></svg>
    <span class="contacts__address">Halden House<br>52 Quarry Lane, Westmead NSW 2145</span>
  </div>

  <div class="back__base"></div>
</section>

</body>
</html>
```